IT Company needs stationary design

Business cards, MS Word, PowerPoint, A4 notepad design base on our company logo. This must be a set of templates in the same style which could be used both for printable documents as well as for documents shared digitally via email, website etc. This should be a modern design which is still professional, so make sure content is well readable both in MS Word and MS PowerPoint templates.
Updates

Target Market(s)

SME and Corporate

Industry/Entity Type

It Company

Font styles to use
Sans Serif

Colors
0455a3
0692cd
f37122
ffc214

Requirements
Must have
• 1) Business cards design: modern but still professional
• 2) MS Word: mostly for IT project documents (business analysis, reports, specifications, etc.) must be professional and easy readable.
• 3) MS PowerPoint: first slide, normal slide, last slide.
• 4) A4 notepad: header (must), footer (must), some light design on the background (optionally)
Nice to have
• Business cards design: would be nice to have 2-4 color variations of the same design from one side - cover (for example part of the cards are blue, part of the cards are orange) and other side with contact details is identical.

```html
<!DOCTYPE html>
<html lang="en">
<head>
<meta charset="utf-8">
<title>corvanta stationery set</title>
<link rel="stylesheet" href="https://fonts.googleapis.com/css2?family=Open+Sans:wght@400;600&display=swap">
<style>
:root{
  --ink:#222;
  --muted:#555;
  --paper:#fff;
  --side-top:#f4f4f4;
  --side-bottom:#c9c9c9;
  --black:#0c0c0c;
  --blue-dark:#0455a3;
  --blue:#0692cd;
  --orange:#f37122;
  --yellow:#ffc214;
  --rule:#bdbdbd;
  --stage:#ffffff;
}
*{box-sizing:border-box;margin:0;padding:0}
html,body{width:1000px;height:1200px;overflow:hidden;background:var(--stage)}
body{position:relative;font-family:"Open Sans",Arial,sans-serif;color:var(--ink)}
.sheet{position:absolute;background:var(--paper);overflow:hidden}
.sheet-side{position:absolute;left:0;top:0;bottom:0;width:80px;background:linear-gradient(180deg,var(--side-top),var(--side-bottom))}
.pattern{position:absolute;background:linear-gradient(160deg,rgba(0,0,0,.05),rgba(0,0,0,0))}
.brand{position:absolute;display:flex;align-items:center;gap:8px;font-size:22px;font-weight:400;color:#333;letter-spacing:.3px}
.brand-dot{width:30px;height:30px;border-radius:50%;border:3px solid var(--blue)}
.brand.light{color:#fff}
.brand.light .brand-dot{border-color:var(--orange)}
.side-address{position:absolute;left:0;width:80px;text-align:center;font-size:5.6px;line-height:1.45;color:#333}
.side-address b{display:block;font-size:6.3px;font-weight:600;line-height:1.25}
.contacts{position:absolute;display:grid;grid-template-columns:auto auto;column-gap:10px;row-gap:2px;font-size:5.6px;color:#333}
.contacts span{padding-left:5px;border-left:2px solid}
.c-orange{border-color:var(--orange)!important}
.c-blue{border-color:var(--blue)!important}
.c-yellow{border-color:var(--yellow)!important}
.c-red{border-color:#d6302a!important}
.letter{position:absolute;left:88px;top:97px;width:210px;font-size:5.4px;line-height:1.45;color:#333}
.letter p{margin-bottom:6px;text-align:justify}
.signature{width:60px;height:22px;background:linear-gradient(90deg,#ddd,#eee);margin-top:4px}
.notes-title{position:absolute;left:84px;top:130px;font-size:14px;font-weight:600;color:#333}
.notes-lines{position:absolute;left:84px;top:145px;width:216px;height:270px;
  background:repeating-linear-gradient(180deg,transparent 0 8px,var(--rule) 8px 9px)}
.dark-panel{position:absolute;left:80px;top:0;right:0;bottom:0;background:var(--black)}
.contacts.light{color:#ddd}
.slide{position:absolute;overflow:hidden;background:linear-gradient(180deg,#f7f7f7,#dedede);box-shadow:0 2px 6px rgba(0,0,0,.25)}
.slide-banner{position:absolute;background:var(--black)}
</style>
</head>
<body>

<!-- Letterhead -->
<section class="sheet letterhead" style="left:12px;top:38px;width:314px;height:442px">
  <div class="sheet-side"></div>
  <div class="pattern" role="img" aria-label="faint triangle line pattern" style="left:0;top:0;width:140px;height:200px"></div>
  <div class="brand" style="left:140px;top:30px"><span class="brand-dot"></span>corvanta</div>
  <div class="letter">
    <p>To the General Director,<br>corvanta Group Limited.<br>20 / 07 / 2014</p>
    <p style="margin-top:10px">Dear Sir / Madam</p>
    <p>Lorem ipsum dolor sit amet, consectetuer adipiscing elit. Nam cursus. Morbi ut mi. Lorem enim leo, egestas id, condimentum at, laoreet mattis, massa. Sed eleifend nonummy diam. Praesent mauris ante, elementum et, bibendum at, posuere sit amet, nibh. Duis tincidunt lectus quis dui viverra vestibulum. Suspendisse vulputate aliquam dui. Nulla elementum dui ut augue. Aliquam vehicula mi at mauris. Maecenas placerat sem si at consequat rhoncus, sem nunc gravida justo.</p>
    <p>Sed laoreet aliquamlii amet, consectetuer adipiscing elit. Nam cursus. Morbi ut mi. Lorem enim leo, egestas id, condimentum at, laoreet mattis, massa. Sed eleifend nonummy diam. Praesent mauris ante, elementum et, bibendum at.</p>
    <p>Nulla elementum dui ut augue, consectetuer adipiscing elit. Nam cursus. Morbi ut mi. Lorem enim leo, egestas id, condimentum at, laoreet mattis, massa. Sed eleifend nonummy diam. Praesent mauris ante, elementum et, bibendum at, posuere sit amet, nibh. Duis tincidunt lectus quis dui viverra vestibulum. Suspendisse vulputate aliquam dui. Nulla elementum dui ut augue. Aliquam vehicula mi at mauris. Maecenas placerat sem si at consequat rhoncus, sem nunc gravida justo. Fusce suscipit varius mi. Cum sociis tes, nascetur ridiculus mus. Nulla dui. Morbi nunc odio, gravida at, cursus nec, luctus lorem. Maecenas tristique orci ac sem. Duis ultricies pharetra magna. Donec accumsan malesuada orci. Donec.</p>
    <p>Iiquam vehicula mi at mauris. Maecenas placerat se si at consequat rhoncus, sem nunc gravida justo. Fusce suscipit varius mi. Cum sociis tes, nascetur ridiculus mus. Nulla dui. Morbi nunc odio, gravida at, cursus nec, luctus lorem. Maecenas tristique orci ac sem amin deso as.</p>
    <p style="margin-top:10px">Sincerely,</p>
    <p>corvanta.</p>
    <div class="signature" role="img" aria-label="handwritten signature"></div>
  </div>
  <div class="side-address" style="top:390px"><b>corvanta<br>SYSTEMS</b>West 18th Avenue<br>2nd Floor<br>Portland, OR 204, USA</div>
  <div class="contacts" style="left:95px;top:406px">
    <span class="c-orange">612 38 74 20</span><span class="c-yellow">www.corvanta.net</span>
    <span class="c-blue">615 92 40 17</span><span class="c-red">hello@corvanta.net</span>
  </div>
</section>

<!-- Notepad -->
<section class="sheet notepad" style="left:338px;top:38px;width:314px;height:442px">
  <div class="sheet-side"></div>
  <div class="pattern" role="img" aria-label="faint triangle line pattern" style="left:0;top:0;width:140px;height:200px"></div>
  <div class="brand" style="left:140px;top:30px"><span class="brand-dot"></span>corvanta</div>
  <div class="notes-title">Notes:</div>
  <div class="notes-lines"></div>
  <div class="side-address" style="top:398px"><b>corvanta<br>SYSTEMS</b>West 18th Avenue<br>2nd Floor<br>Portland, OR 204, USA</div>
  <div class="contacts" style="left:95px;top:406px">
    <span class="c-orange">612 38 74 20</span><span class="c-yellow">www.corvanta.net</span>
    <span class="c-blue">615 92 40 17</span><span class="c-red">hello@corvanta.net</span>
  </div>
</section>

<!-- Cover -->
<section class="sheet cover" style="left:670px;top:38px;width:315px;height:442px">
  <div class="sheet-side"></div>
  <div class="dark-panel"></div>
  <div class="pattern" role="img" aria-label="faint grey triangle pattern on black" style="left:80px;top:60px;right:0;bottom:0;background:linear-gradient(200deg,rgba(255,255,255,.07),rgba(255,255,255,0))"></div>
  <div class="brand light" style="left:140px;top:35px"><span class="brand-dot"></span>corvanta</div>
  <div class="side-address" style="top:390px"><b>corvanta<br>SYSTEMS</b>West 18th Avenue<br>2nd Floor<br>Portland, OR 204, USA</div>
  <div class="contacts light" style="left:95px;top:406px">
    <span class="c-orange">612 38 74 20</span><span class="c-yellow">www.corvanta.net</span>
    <span class="c-blue">615 92 40 17</span><span class="c-red">hello@corvanta.net</span>
  </div>
</section>

<!-- Slides -->
<section class="slide slide-normal" style="left:272px;top:617px;width:630px;height:471px">
  <div class="pattern" role="img" aria-label="dashed triangle line pattern, left edge" style="left:0;top:0;width:110px;height:471px"></div>
  <div class="pattern" role="img" aria-label="dashed triangle line pattern, upper right" style="left:350px;top:0;width:280px;height:330px;background:linear-gradient(200deg,rgba(0,0,0,.06),rgba(0,0,0,0))"></div>
</section>

<section class="slide slide-first" style="left:464px;top:963px;width:246px;height:184px">
  <div class="slide-banner" style="left:44px;top:0;right:0;height:71px"></div>
  <div class="brand light" style="left:60px;top:20px;font-size:20px"><span class="brand-dot" style="width:26px;height:26px"></span>corvanta</div>
  <div class="side-address" style="left:0;top:146px;width:44px;font-size:3.6px"><b style="font-size:4px">corvanta<br>SYSTEMS</b>West 18th Avenue<br>2nd Floor<br>Portland, OR 204</div>
  <div class="contacts" style="left:54px;top:156px;font-size:5.4px">
    <span class="c-orange">612 38 74 20</span><span class="c-yellow">www.corvanta.net</span>
    <span class="c-blue">615 92 40 17</span><span class="c-red">hello@corvanta.net</span>
  </div>
</section>

<section class="slide slide-last" style="left:715px;top:963px;width:245px;height:184px">
  <div class="pattern" role="img" aria-label="dashed triangle line pattern" style="left:120px;top:0;width:125px;height:120px"></div>
  <div class="brand" style="left:6px;top:158px;font-size:10px;gap:4px"><span class="brand-dot" style="width:14px;height:14px;border-width:2px"></span>corvanta</div>
</section>

</body>
</html>
```